Renewable Energy Consultancy needs relatively simple but smart website

We are a renewable energy focussed consultancy called Bellmoran, and we are just starting out. Our target is to bring knowledge of the detailed technical and commercial operations of renewables projects, mainly wind energy.

Our target customers are major energy utilities and private finance groups, who look to invest in renewables projects as a long term money-earning system. We are a fairly young, dynamic team of industry-respected people (4 of us) but we need to make ourselves look bigger than this (our customers will expect us to take on major projects, so we need to look big enough to handle it...)

We're not going to sell anything from our website and we expect it to just support our company name. Most of our customers are made by strong networks and relationships, so its mainly there to give confidence in our capabilities and give a strong view of who we are. We probably need a site with 4/5 pages which we can then expand when needed.

We have logos and headers (attached) which we want to use (also run through artpitchly), and I've attached a few pictures of projects similar to those we will be involved in to give us a feel for how it will look. Also attached are the colours we liked which are now used in the logo, and the font details. Whilst we're a "green" company with a "green" logo, we don't want to be completely green, so some nice combinations of colours on the pages would be good.

Ideally we need to have chirpnet/workgrid news feeds somewhere linked into the site.

The design should be smart - giving a feel of high integrity and assurance whilst making us seem approachable and knowledgeable.

Target Market(s)

Renewables investors, developers of renewables projects (wind farms etc),

Industry/Entity Type

Finance

Coding

Coded - Design and coding required

Number of Pages Required

4 page

Other font styles liked:
• See the attachment with brand text/colour details ("colour codes" filename)

Requirements
Must have
• A fairly simple, but smart website design. We're looking to provide confidence and consolidate our networks with the website, not specifically find new customers - so its really just to give customers somewhere they can relate to online
Nice to have
• We have logos/brands and colours - so a website which incorperates these well and brings accross a professional company
• Would be nice to have a page (such as a blog/wordpress) we can easily update with news/events etc and links to chirpnet feed and workgrid feed ideally.
Should not have
• cartoons, flashy gimmicks,

```html
<!DOCTYPE html>
<html lang="en">
<head>
<meta charset="utf-8">
<title>Bellmoran Renewable Energy Consultancy</title>
<link rel="stylesheet" href="https://fonts.googleapis.com/css2?family=Montserrat:wght@400;600;700;800&family=Open+Sans:wght@400;600;700&display=swap">
<style>
:root{
  --green:#2e7d0f;
  --green-dark:#1b4a07;
  --green-bright:#6bb51f;
  --orange:#f26b10;
  --grey-btn:#4a4a4a;
  --ink:#333;
  --muted:#666;
  --panel:#eeeeee;
  --line:#d9d9d9;
  --footer:#1d4a05;
  --footer-bar:#2a2a2a;
  --sea-top:#244a72;
  --sea-bottom:#1a3556;
}
*{box-sizing:border-box;margin:0;padding:0}
html,body{width:1200px;height:3066px;overflow:hidden}
body{position:relative;font-family:"Open Sans",Arial,sans-serif;color:var(--ink);background:#fff}
.abs{position:absolute}
.heading{font-family:"Montserrat",Arial,sans-serif}

/* header */
.site-header{left:0;top:0;width:1200px;height:51px;background:#fff;border-bottom:1px solid var(--line)}
.brand{left:188px;top:8px;display:flex;align-items:center;gap:12px}
.brand-dot{width:32px;height:32px;border-radius:50%;background:var(--green)}
.brand-name{font-family:"Montserrat",sans-serif;font-size:25px;color:#555;font-weight:400}
.main-nav{left:432px;top:17px;display:flex;gap:16px;font-size:14px;font-weight:600;color:#333}
.main-nav .active{color:var(--green-bright)}
.nav-tab{left:988px;top:0;width:24px;height:40px;background:#555}

/* hero */
.hero{left:0;top:51px;width:1200px;height:552px;background:linear-gradient(180deg,var(--sea-top),var(--sea-bottom))}
.hero-title{left:0;top:188px;width:1200px;text-align:center;color:#fff;font-family:"Montserrat",sans-serif;font-weight:700;font-size:38px;line-height:48px}
.hero-dash{left:590px;top:162px;width:22px;height:3px;background:#fff}
.btn-consult{left:476px;top:304px;width:248px;height:38px;background:#6bb51f;color:#fff;font-weight:600;font-size:17px;text-align:center;line-height:38px}
.hero-links{left:0;top:376px;width:1200px;display:flex;justify-content:center;gap:24px;color:#fff;font-size:12px;align-items:center}
.hero-links span{display:flex;align-items:center;gap:8px}
.play{width:18px;height:18px;border-radius:50%;background:#fff}
.sep{width:2px;height:22px;background:#fff}
.dots{left:586px;top:466px;display:flex;gap:5px}
.dots i{width:10px;height:10px;border-radius:50%;background:#555}
.dots i:first-child{background:#fff}
.quote-bar{left:0;top:560px;width:1200px;height:43px;background:rgba(15,15,20,.85);color:#fff;font-size:12px}
.quote-text{left:188px;top:13px}
.quote-nav{left:976px;top:13px;display:flex;gap:4px}
.quote-nav i{width:16px;height:16px;border-radius:50%;background:#fff}

/* section shared */
.section-title{width:1200px;left:0;text-align:center;font-family:"Montserrat",sans-serif;font-size:27px}
.divider{left:528px;width:144px;height:20px;display:flex;align-items:center;gap:8px}
.divider b{flex:1;border-top:1px dashed #888}
.divider i{width:18px;height:18px;border-radius:50%;background:var(--green)}
.btn{display:block;width:90px;height:20px;line-height:20px;font-size:10px;color:#fff;text-align:center;background:var(--grey-btn)}
.btn.is-hot{background:var(--orange)}

/* services */
.services-title{top:678px;color:#444;font-weight:500}
.service{top:790px;width:300px;text-align:center}
.service-ring{margin:0 auto;width:184px;height:184px;border-radius:50%;border:2px solid #eee;display:flex;align-items:center;justify-content:center}
.service-ring i{width:110px;height:110px;border-radius:50%;background:linear-gradient(180deg,#3f9a12,#1c5a05)}
.service h3{margin-top:32px;font-size:15px;color:var(--green-dark);font-weight:700}
.service p{margin:4px auto 0;width:240px;font-size:12px;line-height:18px;color:var(--muted)}
.service .btn{margin:10px auto 0}

/* projects */
.projects{left:0;top:1186px;width:1200px;height:552px;background:var(--panel);border-top:1px solid var(--line);border-bottom:1px solid var(--line)}
.projects-title{top:1264px;color:var(--green-dark);font-weight:700}
.project{top:1367px;width:258px}
.project-photo{width:258px;height:170px}
.project h3{margin-top:18px;font-size:15px;font-weight:700;color:#444}
.project p{margin-top:4px;font-size:12px;line-height:18px;color:var(--muted)}
.project .btn{margin-top:10px}
.carousel-arrow{top:1487px;width:16px;height:26px;background:#ddd;border:1px solid #ccc}

/* locations & news */
.card{background:#fff;border:1px solid #ddd;padding:18px}
.card h2{font-family:"Montserrat",sans-serif;font-size:17px;font-weight:600;color:var(--green-dark);padding-bottom:12px;border-bottom:1px dashed #bbb}
.locations{left:188px;top:1795px;width:560px;height:362px}
.map{margin-top:18px;width:522px;height:262px;background:linear-gradient(135deg,#e4e8d6,#cfdcb8 55%,#e8e3d0)}
.map-pin{left:257px;top:1972px}
.news{left:762px;top:1795px;width:252px;height:362px}
.news-item{margin-top:18px;border-bottom:1px dotted #ccc;padding-bottom:8px}
.news-date{display:inline-block;background:#ddd;font-size:9px;color:#555;padding:2px 22px 2px 10px}
.news-item p{margin-top:6px;font-size:11px;line-height:17px;color:var(--muted)}
.view-all{text-align:right;margin-top:8px;font-size:11px;color:var(--orange)}

/* team */
.team{left:0;top:2218px;width:1200px;height:501px;background:linear-gradient(180deg,#9a9a9a,#6e6e6e 60%,#5a5a5a)}
.team-kicker{top:2330px;left:0;width:1200px;text-align:center;color:#fff;font-family:"Montserrat",sans-serif;font-weight:700;font-size:36px}
.team-divider{top:2388px;left:536px}
.team-divider b{border-top-color:#fff}
.team-divider i{background:#fff}
.team-big{top:2410px;left:0;width:1200px;text-align:center;color:#fff;font-family:"Montserrat",sans-serif;font-weight:700;font-size:104px;line-height:120px;letter-spacing:1px}
.team-text{top:2528px;left:380px;width:440px;text-align:center;color:#fff;font-size:14px;line-height:18px}
.team-btn{top:2598px;left:555px}

/* footer */
.footer{left:0;top:2719px;width:1200px;height:286px;background:var(--footer);color:#fff}
.footer h4{font-size:14px;font-weight:700;margin-bottom:18px}
.footer ul{list-style:none;font-size:10px;line-height:22px}
.footer li::before{content:"› ";}
.quick{left:188px;top:2800px}
.quick-cols{display:flex;gap:60px}
.svc{left:416px;top:2800px}
.signup{left:620px;top:2800px}
.signup input{display:block;width:174px;height:24px;border:1px solid #ccc;font-size:10px;padding:0 6px;margin-bottom:7px;font-family:inherit}
.signup .btn{width:116px;height:26px;line-height:26px;font-size:11px;font-weight:600;background:var(--orange)}
.footer-brand{left:868px;top:2800px;display:flex;align-items:center;gap:10px}
.footer-brand i{width:42px;height:42px;border-radius:50%;background:#fff}
.footer-brand span{font-family:"Montserrat",sans-serif;font-size:24px;color:#fff}
.footer-bar{left:0;top:3005px;width:1200px;height:61px;background:var(--footer-bar);color:#ddd;font-size:10px}
.copyright{left:188px;top:24px}
.social{left:614px;top:18px;display:flex;gap:6px}
.social i{width:24px;height:24px;border-radius:50%;border:1px solid #aaa}
</style>
</head>
<body>

<header class="site-header abs">
  <div class="brand abs"><i class="brand-dot"></i><span class="brand-name">Bellmoran</span></div>
  <nav class="main-nav abs">
    <span>Home</span><span class="active">About</span><span>Projects</span><span>Events/Blogs</span><span>Services</span><span>Team</span><span>Costumers</span><span>Contact</span>
  </nav>
  <div class="nav-tab abs"></div>
</header>

<section class="hero abs" role="img" aria-label="Offshore wind farm turbines standing in the open sea, seen from above"></section>
<div class="hero-dash abs"></div>
<h1 class="hero-title abs">Welcome to Bellmoran Renewable<br>Energy Consultancy</h1>
<div class="btn-consult abs">Get Free Consultation</div>
<div class="hero-links abs"><span><i class="play"></i>Video</span><i class="sep"></i><span><i class="play"></i>Learn More</span></div>
<div class="dots abs"><i></i><i></i><i></i></div>
<div class="quote-bar abs">
  <p class="quote-text abs">“ Lorem ipsum dolor sit amet, consectetur adipisicing elit, sed do eiusmod tempor ” &nbsp; Jonh Doe - USA</p>
  <div class="quote-nav abs"><i></i><i></i></div>
</div>

<h2 class="section-title services-title abs">Our Product/Service Information</h2>
<div class="divider abs" style="top:726px"><b></b><i></i><b></b></div>
<div class="service abs" style="left:157px"><div class="service-ring"><i></i></div><h3>Wind Energy</h3><p>Lorem ipsum dolor sit amet, consectetur adipisicing elit, sed do eiusmod</p><span class="btn is-hot">Learn More</span></div>
<div class="service abs" style="left:449px"><div class="service-ring"><i></i></div><h3>Energy Consultancy</h3><p>Lorem ipsum dolor sit amet, consectetur adipisicing elit, sed do eiusmod</p><span class="btn">Learn More</span></div>
<div class="service abs" style="left:745px"><div class="service-ring"><i></i></div><h3>Research and Development</h3><p>Lorem ipsum dolor sit amet, consectetur adipisicing elit, sed do eiusmod</p><span class="btn">Learn More</span></div>

<section class="projects abs"></section>
<h2 class="section-title projects-title abs">Company Projects</h2>
<div class="divider abs" style="top:1320px"><b></b><i></i><b></b></div>
<div class="carousel-arrow abs" style="left:145px"></div>
<div class="carousel-arrow abs" style="left:1036px"></div>
<article class="project abs" style="left:188px">
  <div class="project-photo" role="img" aria-label="Turbine installation vessel with crane at a harbour" style="background:linear-gradient(180deg,#b9cde4,#8a8f96 55%,#8a3b36)"></div>
  <h3>Lorem ipsum our service</h3><p>Lorem ipsum dolor sit amet, adipisicing elit, sed do eiusmod</p><span class="btn is-hot">Learn More</span>
</article>
<article class="project abs" style="left:470px">
  <div class="project-photo" role="img" aria-label="Wind turbines silhouetted against a sunset sky" style="background:linear-gradient(180deg,#2c3fa0,#c0392b 55%,#f0a030 75%,#1a1a1a)"></div>
  <h3>Lorem ipsum our service</h3><p>Lorem ipsum dolor sit amet, adipisicing elit, sed do eiusmod</p><span class="btn">Learn More</span>
</article>
<article class="project abs" style="left:756px">
  <div class="project-photo" role="img" aria-label="Offshore turbine under construction at sea" style="background:linear-gradient(180deg,#c3cfd8,#6f8394 60%,#3f5566)"></div>
  <h3>Lorem ipsum our service</h3><p>Lorem ipsum dolor sit amet, adipisicing elit, sed do eiusmod</p><span class="btn">Learn More</span>
</article>

<section class="card locations abs">
  <h2>Our Locations</h2>
  <div class="map" role="img" aria-label="Road map of the office region with a location marker"></div>
</section>
<svg class="map-pin abs" width="48" height="64" viewBox="0 0 48 64" aria-hidden="true"><path d="M24 2C12 2 3 11 3 23c0 15 21 39 21 39s21-24 21-39C45 11 36 2 24 2z" fill="#1f5a0a"/><circle cx="24" cy="22" r="9" fill="#fff"/></svg>

<aside class="card news abs">
  <h2>News and Events</h2>
  <div class="news-item"><span class="news-date">13 Mar, 2015</span><p>Lorem ipsum dolor sit amet consec tetur adipisicing elit</p></div>
  <div class="news-item"><span class="news-date">13 Mar, 2015</span><p>Lorem ipsum dolor sit amet consec tetur adipisicing elit</p></div>
  <div class="news-item"><span class="news-date">13 Mar, 2015</span><p>Lorem ipsum dolor sit amet consec tetur adipisicing elit</p></div>
  <p class="view-all">View All ➜</p>
</aside>

<section class="team abs" role="img" aria-label="Blurred group photo of the consultancy team standing together"></section>
<h2 class="team-kicker abs">Meet Our Team</h2>
<div class="divider team-divider abs"><b></b><i></i><b></b></div>
<p class="team-big abs">MEMBERS</p>
<p class="team-text abs">Lorem ipsum dolor sit amet consec tetur adipisicing elit, do eiusmod consecadipisicing</p>
<span class="btn is-hot team-btn abs">Click Here</span>

<footer class="footer abs"></footer>
<div class="quick abs" style="color:#fff">
  <h4 style="font-size:14px;margin-bottom:18px">Quick Links</h4>
  <div class="quick-cols">
    <ul style="list-style:none;font-size:10px;line-height:22px"><li>› Home</li><li>› About Us</li><li>› Blogs/Events</li><li>› Services</li><li>› Projects</li></ul>
    <ul style="list-style:none;font-size:10px;line-height:22px"><li>› Our Team</li><li>› Blogs</li><li>› Customers</li><li>› Contact Us</li><li>› Testimonials</li></ul>
  </div>
</div>
<div class="svc abs" style="color:#fff">
  <h4 style="font-size:14px;margin-bottom:18px">Our Services</h4>
  <ul style="list-style:none;font-size:10px;line-height:22px"><li>› Renewable Energy</li><li>› Energy Consultancy</li><li>› Wind Power Plants</li><li>› Research and Development</li></ul>
</div>
<div class="signup abs" style="color:#fff">
  <h4 style="font-size:14px;margin-bottom:18px">Signup for Blog Update</h4>
  <input type="text" placeholder="Enter Name">
  <input type="text" placeholder="Enter Email-ID">
  <span class="btn" style="width:116px;height:26px;line-height:26px;font-size:11px;font-weight:600;background:var(--orange)">Subscribe Me</span>
</div>
<div class="footer-brand abs"><i></i><span>Bellmoran</span></div>

<div class="footer-bar abs">
  <p class="copyright abs">All Right Reserved © 2015 with Bellmoran &nbsp;Terms &amp; Condition</p>
  <div class="social abs"><i></i><i></i><i></i></div>
</div>

</body>
</html>
```